Futuristic Trade Show Booth Design for Quell Builders, Quell Designers, and Quell Corporate

We are seeking a cutting-edge and visually striking trade show booth design that showcases the synergy between our three brands: Quell Designers (architectural design), Quell Builders (construction services), and Quell Corporate (unified identity). The design must reflect our commitment to innovation, professionalism, and forward-thinking solutions for commercial design and construction.

The booth will include three panels and two podiums, with a modern and futuristic aesthetic. The focus is on creating a cohesive yet distinctive identity for each brand while highlighting their integration under Quell Corporate. Here’s what we envision:

Booth Specifications:
Backdrop Dimensions: Three panels of equal size.
Podiums: Two, one representing Quell Designers and the other Quell Builders.
Color Palette: Red (#D00E07), dark gray (#3B3838), light gray (#E0E0E0), and white (#FFFFFF).
Panel Breakdown:
1. Left Panel: Quell Designers (Architectural Focus)

Content:
Taglines like “Design Smarter”
Highlight Quell Designers’ architectural services : Commercial Architecture, Space Planning, Interior Design, Master Planning, 3D Renderings).
Visuals:
Include high-resolution 3D renderings of commercial spaces and modern blueprints.
Use a gradient background (dark gray to light gray) with overlays of translucent grids.
Icons representing architectural precision (e.g., drafting tools, rulers).
2. Center Panel: Quell Corporate (Unified Identity)
Content:
Central tagline: “Intergrated Design-Build Solution”
Unified messaging emphasizing Quell Corporate’s leadership in integrated design-build services.
Showcase how Quell Designers and Quell Builders collaborate seamlessly under Quell Corporate.
Visuals:
A split image showing half blueprints (design) and half construction (build).
Gradient background transitioning from red to gray for continuity.
Icons or a flowchart highlighting the steps: “Concept > Design > Build > Completion.”
3. Right Panel: Quell Builders (Construction Focus)

Content:
Taglines like “BUILD SMARTER
Highlight Quell Builders’ construction services (Construction Management, Design-Build, General Contracting, Pre-Construction).
Visuals:

Overlay dynamic construction elements like cranes, scaffolding, and hard hats.
LED accents or subtle motion graphics to emphasize innovation.
Podium Design:
Quell Designers Podium:
Gray-themed with the Quell Designers logo and tagline: “DESIGN SMARTER”
Quell Builders Podium:
Red-themed with the Quell Builders logo and tagline: “BUILD SMARTER.”
Design Requirements:
Must reflect a modern and futuristic aesthetic.
Use clean, bold typography (e.g., Yantramanav or similar).
Ensure cohesive branding across all panels while keeping individual identities for Quell Designers, Quell Builders, and Quell Corporate.
Balance professionalism with engaging visuals to attract visitors at the trade show.
Additional Notes:
The booth will serve as a centerpiece for showcasing Quell Corporate’s integrated approach to commercial design and construction. The design must communicate trust, innovation, and expertise while captivating the audience at first glance.

Quell Builders Website: www.quellbuilders.example
Quell Designers Website: www.quelldesigners.example
Quell Corporate: www.quellcorporate.example
Logo Quell Builders: https://files.example.net/share/a8Tq3LmZ0pWv7RcYx2NbK5sJd9HfGu4Ee
Logo Quell Designers: https://files.example.net/share/b3Kw8NpR1tYh6QdXz0MaL4cVf7JgSe2Uu
Logo Quell Corporate: https://files.example.net/share/c5Rn2HtB9wXk4PfVy1LdM8aZq6GjTo3Ii
The booth information and spec is on : https://www.standvelo.example/stand-ideas/linkup-10x10-stands/linkup-10x10-expo-stand-kit-c/

Target Market(s)

Commercial Property Developers, Corporate Real Estate Managers, Franchise Construction VP, Retail Franchise Owners,

Industry/Entity Type

Commercial Construction, Commercial Architecture

Font styles to use
Other font styles liked:
• Open to others but like Yantramanav, Poppins, Montserrat

Colors
EB3D1F
EC4F4E
F09395
F8D3D4
FCEDEE

Requirements
Must have
• Clear and prominent branding for Quell Designers, Quell Builders, and Quell Corporate on their respective panels. Consistent color scheme using red (#D00E07), dark gray (#3B3838), light gray (#E0E0E0), and white (#FFFFFF) to unify the design. A modern and futuristic aesthetic that reflects innovation, precision, and professionalism. Distinct yet cohesive representation of services offered by Quell Designers (architectural design), Quell Builders (construction), and Quell Corporate (integrated solutions).
Nice to have
• Subtle motion graphics or holographic overlays on panels to enhance the modern feel. A unified gradient background transitioning from red to gray to connect all panels visually. Visual flowcharts showing the step-by-step process of design-build services. Interactive design elements such as QR codes
Should not have
• Overly cluttered design that detracts from key messages or visuals. Fonts that are hard to read or do not match the modern and professional aesthetic. Excessive use of unrelated colors or mismatched visual styles. Misalignment or lack of clear separation between Quell Designers, Quell Builders, and Quell Corporate branding.

```html
<!DOCTYPE html>
<html lang="en">
<head>
<meta charset="utf-8">
<title>Quell Trade Show Booth Panels</title>
<link rel="stylesheet" href="https://fonts.googleapis.com/css2?family=Roboto:ital,wght@0,400;0,500;0,700;1,700&display=swap">
<style>
  :root {
    --red: #d00e07;
    --red-deep: #a3161a;
    --maroon: #7a3a3c;
    --dark: #3b3838;
    --slate: #4d4b4b;
    --light: #e0e0e0;
    --white: #ffffff;
    --stage: #ececec;
    --blush: #f8d3d4;
  }
  html, body {
    margin: 0;
    width: 1200px;
    height: 853px;
    overflow: hidden;
    background: var(--stage);
  }
  .booth {
    position: absolute;
    left: 97px;
    top: 53px;
    width: 975px;
    height: 747px;
    filter: drop-shadow(0 6px 14px rgba(0,0,0,0.35));
  }
  .booth text { font-family: "Roboto", Arial, sans-serif; }
  .brand-name { font-size: 17px; font-weight: 500; letter-spacing: 4.5px; fill: var(--dark); }
  .brand-name--lead { font-size: 23px; letter-spacing: 5.5px; }
  .tagline { font-size: 42px; font-weight: 700; fill: var(--white); }
  .tagline .accent { font-style: italic; }
  .headline { font-size: 38px; font-weight: 700; fill: var(--white); }
  .service { font-size: 21px; font-weight: 500; fill: var(--dark); }
  .step-num { font-size: 40px; font-weight: 500; fill: var(--white); }
  .step-label { font-size: 15px; font-weight: 500; fill: var(--white); }
  .brand-tab { font-size: 21px; font-weight: 500; fill: var(--white); }
  .icon { fill: none; stroke: var(--red); stroke-width: 2.2; stroke-linejoin: round; }
</style>
</head>
<body>
<svg class="booth" viewBox="182 100 1828 1400" xmlns="http://www.w3.org/2000/svg">
  <defs>
    <linearGradient id="grayFade" x1="0" y1="0" x2="0" y2="1">
      <stop offset="0" stop-color="#5d5b5b"/>
      <stop offset="0.6" stop-color="#6b6969"/>
      <stop offset="1" stop-color="#8d8b8b"/>
    </linearGradient>
    <radialGradient id="haze" cx="0.5" cy="0.4" r="0.6">
      <stop offset="0" stop-color="#ffffff" stop-opacity="0.28"/>
      <stop offset="1" stop-color="#ffffff" stop-opacity="0"/>
    </radialGradient>
    <linearGradient id="lightFade" x1="0" y1="0" x2="0" y2="1">
      <stop offset="0" stop-color="#9a9898"/>
      <stop offset="0.5" stop-color="#c2c1c1"/>
      <stop offset="1" stop-color="#e6e6e6"/>
    </linearGradient>
    <linearGradient id="blushFade" x1="0" y1="0" x2="1" y2="1">
      <stop offset="0" stop-color="#f3dede"/>
      <stop offset="0.5" stop-color="#fbf1f1"/>
      <stop offset="1" stop-color="#eec8c8"/>
    </linearGradient>
    <linearGradient id="maroonBox" x1="0" y1="0" x2="1" y2="0">
      <stop offset="0" stop-color="#6b3c3e"/>
      <stop offset="1" stop-color="#8c3a3c"/>
    </linearGradient>
    <linearGradient id="redFade" x1="0" y1="0" x2="1" y2="1">
      <stop offset="0" stop-color="#d01a1c"/>
      <stop offset="0.5" stop-color="#b8181b"/>
      <stop offset="1" stop-color="#a5191c"/>
    </linearGradient>
    <linearGradient id="wineFade" x1="0" y1="0" x2="1" y2="1">
      <stop offset="0" stop-color="#9a3436"/>
      <stop offset="0.5" stop-color="#8b3638"/>
      <stop offset="1" stop-color="#a54a4c"/>
    </linearGradient>
    <linearGradient id="lobbyTone" x1="0" y1="0" x2="0" y2="1">
      <stop offset="0" stop-color="#7f7e7e"/>
      <stop offset="0.25" stop-color="#d6d6d6"/>
      <stop offset="0.6" stop-color="#eeeeee"/>
      <stop offset="1" stop-color="#8f8585"/>
    </linearGradient>
    <radialGradient id="lobbyAccent" cx="0.8" cy="0.85" r="0.3">
      <stop offset="0" stop-color="#d00e07" stop-opacity="0.55"/>
      <stop offset="1" stop-color="#d00e07" stop-opacity="0"/>
    </radialGradient>
    <linearGradient id="buildingTone" x1="0" y1="0" x2="1" y2="0">
      <stop offset="0" stop-color="#ececec"/>
      <stop offset="0.45" stop-color="#8d949b"/>
      <stop offset="0.7" stop-color="#4f5a66"/>
      <stop offset="1" stop-color="#c06a36"/>
    </linearGradient>
    <linearGradient id="buildingSky" x1="0" y1="0" x2="0" y2="1">
      <stop offset="0" stop-color="#cfd8e0" stop-opacity="0.6"/>
      <stop offset="0.4" stop-color="#ffffff" stop-opacity="0"/>
      <stop offset="1" stop-color="#f2f2f2" stop-opacity="0.7"/>
    </linearGradient>
    <linearGradient id="siteTone" x1="0" y1="0" x2="1" y2="1">
      <stop offset="0" stop-color="#1c7aa3"/>
      <stop offset="0.45" stop-color="#4d6a7d"/>
      <stop offset="1" stop-color="#e98a2a"/>
    </linearGradient>
    <radialGradient id="siteGlow" cx="0.65" cy="0.75" r="0.45">
      <stop offset="0" stop-color="#f7a33a" stop-opacity="0.6"/>
      <stop offset="1" stop-color="#f7a33a" stop-opacity="0"/>
    </radialGradient>
  </defs>

  <!-- ===== Left panel: Quell Designers ===== -->
  <g class="panel panel--designers">
    <rect x="182" y="100" width="609" height="1400" fill="var(--white)"/>
    <rect x="182" y="265" width="609" height="320" fill="url(#grayFade)"/>
    <rect x="182" y="265" width="609" height="320" fill="url(#haze)" role="img" aria-label="Translucent architectural floor plan grid over dark gray"/>
    <polygon points="182,100 791,100 791,108 600,108 487,150 375,108 182,108" fill="var(--red)"/>
    <polygon points="420,100 555,100 487,130" fill="var(--dark)"/>
    <polygon points="182,180 791,180 791,265 487,360 182,265" fill="var(--white)"/>
    <polyline points="182,260 487,352 791,260" fill="none" stroke="var(--red)" stroke-width="14"/>
    <polyline points="230,258 487,336 745,258" fill="none" stroke="var(--white)" stroke-width="6"/>
    <rect x="472" y="200" width="30" height="30" fill="var(--red)"/>
    <text class="brand-name" x="487" y="296" text-anchor="middle">QUELL DESIGNERS</text>

    <rect x="182" y="810" width="609" height="690" fill="url(#lightFade)"/>
    <rect x="182" y="810" width="609" height="260" fill="url(#haze)" role="img" aria-label="Translucent blueprint linework over light gray"/>
    <rect x="182" y="1400" width="609" height="100" fill="url(#blushFade)" role="img" aria-label="Red blueprint linework on white"/>

    <polygon points="182,585 219,572 754,572 791,585 791,790 487,885 182,790" fill="var(--white)"/>
    <polyline points="182,580 219,568" fill="none" stroke="var(--red)" stroke-width="8"/>
    <polyline points="754,568 791,580" fill="none" stroke="var(--red)" stroke-width="8"/>
    <rect x="219" y="460" width="535" height="104" fill="url(#maroonBox)" stroke="var(--red)" stroke-width="5"/>
    <text class="tagline" x="487" y="529" text-anchor="middle">DESIGN <tspan class="accent">SMARTER</tspan></text>

    <polygon points="182,800 487,895 791,800 791,815 487,918 182,815" fill="var(--red)"/>
    <polygon points="182,790 487,885 791,790 791,800 487,897 182,800" fill="var(--white)"/>

    <polygon points="182,1070 487,975 791,1070 791,1430 487,1500 182,1430" fill="var(--white)"/>
    <polygon points="182,1080 487,990 791,1080 791,1420 487,1488 182,1420" fill="url(#lobbyTone)"/>
    <polygon points="182,1080 487,990 791,1080 791,1420 487,1488 182,1420" fill="url(#lobbyAccent)" role="img" aria-label="3D rendering of a modern commercial lobby with elevators and red seating"/>
    <polygon points="360,1027 487,990 615,1027" fill="var(--dark)"/>
    <polygon points="360,1445 615,1445 487,1488" fill="var(--dark)"/>

    <g class="services">
      <circle cx="312" cy="630" r="38" fill="#f4f4f4"/>
      <g class="icon"><rect x="290" y="610" width="42" height="42"/><path d="M296 645 L324 612 M300 648 h26 v-20 z"/></g>
      <text class="service" x="361" y="627">Commercial</text>
      <text class="service" x="361" y="657">Architecture</text>

      <circle cx="572" cy="630" r="38" fill="#f4f4f4"/>
      <g class="icon"><path d="M545 632 h54 M572 605 v54 M558 620 h28 v24 h-28 z"/></g>
      <text class="service" x="621" y="627">Space</text>
      <text class="service" x="621" y="657">Planning</text>

      <circle cx="312" cy="727" r="38" fill="#f4f4f4"/>
      <g class="icon"><rect x="288" y="703" width="50" height="50"/><path d="M288 722 h24 M312 703 v34 M312 737 h26 M324 737 v16"/></g>
      <text class="service" x="361" y="722">Interior</text>
      <text class="service" x="361" y="752">Design</text>

      <circle cx="572" cy="727" r="38" fill="#f4f4f4"/>
      <g class="icon"><rect x="548" y="712" width="48" height="36" rx="8"/><circle cx="558" cy="732" r="6"/><circle cx="586" cy="732" r="6"/><path d="M572 700 v30 M566 706 h12"/></g>
      <text class="service" x="621" y="722">Master</text>
      <text class="service" x="621" y="752">Planning</text>

      <circle cx="487" cy="803" r="38" fill="#f4f4f4"/>
      <g class="icon"><path d="M487 780 L512 792 L512 818 L487 830 L462 818 L462 792 Z M462 792 L512 818 M512 792 L462 818 M487 780 v50"/></g>
      <text class="service" x="487" y="856" text-anchor="middle">3D Rendering</text>
    </g>
  </g>

  <!-- ===== Center panel: Quell Corporate ===== -->
  <g class="panel panel--corporate">
    <rect x="791" y="100" width="610" height="1400" fill="var(--white)"/>
    <rect x="791" y="100" width="610" height="30" fill="var(--red)"/>
    <polygon points="985,100 1210,100 1097,145" fill="var(--white)"/>
    <polygon points="1020,100 1175,100 1097,132" fill="var(--dark)"/>
    <rect x="1077" y="215" width="40" height="40" fill="var(--red)"/>
    <text class="brand-name brand-name--lead" x="1097" y="340" text-anchor="middle">QUELL CORPORATE</text>

    <polygon points="791,325 1097,400 1401,325 1401,588 1097,512 791,550" fill="url(#redFade)"/>
    <polygon points="791,325 1097,400 1401,325 1401,588 1097,512 791,550" fill="url(#haze)" opacity="0.6" role="img" aria-label="Red blueprint overlay on red"/>
    <polyline points="791,318 1097,392 1401,318" fill="none" stroke="var(--red)" stroke-width="10"/>
    <polyline points="840,318 1097,380 1355,318" fill="none" stroke="var(--white)" stroke-width="5"/>
    <rect x="831" y="399" width="531" height="99" fill="var(--red)" stroke="var(--white)" stroke-width="3"/>
    <text class="headline" x="1097" y="441" text-anchor="middle">INTERGRATED</text>
    <text class="headline" x="1097" y="486" text-anchor="middle">DESIGN-BUILD SOLUTION</text>

    <polygon points="791,815 1097,920 1401,815 1401,1500 791,1500" fill="url(#wineFade)" role="img" aria-label="Red drafting linework and crane skyline overlay"/>
    <polygon points="791,800 1097,905 1401,800 1401,815 1097,920 791,815" fill="var(--red)"/>

    <g class="flowchart">
      <polygon points="1097,512 1187,602 1097,692 1007,602" fill="var(--slate)"/>
      <polygon points="995,612 1085,702 995,792 905,702" fill="var(--slate)"/>
      <polygon points="1197,612 1287,702 1197,792 1107,702" fill="var(--red)"/>
      <polygon points="1097,712 1187,802 1097,892 1007,802" fill="var(--red)"/>
      <g stroke="var(--white)" stroke-width="1.5">
        <line x1="1037" y1="601" x2="1157" y2="601"/>
        <line x1="935" y1="703" x2="1055" y2="703"/>
        <line x1="1137" y1="703" x2="1257" y2="703"/>
        <line x1="1037" y1="803" x2="1157" y2="803"/>
      </g>
      <text class="step-num" x="1097" y="587" text-anchor="middle">2</text>
      <text class="step-label" x="1097" y="629" text-anchor="middle">Design</text>
      <text class="step-num" x="995" y="688" text-anchor="middle">1</text>
      <text class="step-label" x="995" y="730" text-anchor="middle">Concept</text>
      <text class="step-num" x="1197" y="688" text-anchor="middle">3</text>
      <text class="step-label" x="1197" y="730" text-anchor="middle">Build</text>
      <text class="step-num" x="1097" y="788" text-anchor="middle">4</text>
      <text class="step-label" x="1097" y="830" text-anchor="middle">Completion</text>
    </g>
    <rect x="791" y="548" width="209" height="55" fill="var(--slate)"/>
    <text class="brand-tab" x="893" y="582" text-anchor="middle">Quell Designers</text>
    <rect x="1192" y="800" width="209" height="55" fill="var(--red)"/>
    <text class="brand-tab" x="1296" y="834" text-anchor="middle">Quell Builders</text>

    <polygon points="791,1030 1097,975 1401,1030 1401,1405 1097,1500 791,1405" fill="var(--white)"/>
    <polygon points="791,1040 1097,988 1401,1040 1401,1395 1097,1488 791,1395" fill="url(#buildingTone)"/>
    <polygon points="791,1040 1097,988 1401,1040 1401,1395 1097,1488 791,1395" fill="url(#buildingSky)" role="img" aria-label="Modern commercial building shown half as blueprint sketch and half as completed construction"/>
    <polygon points="970,1027 1097,985 1225,1027" fill="var(--red)"/>
    <polygon points="791,1405 1097,1500 791,1500" fill="var(--slate)"/>
    <polygon points="1401,1405 1097,1500 1401,1500" fill="var(--slate)"/>
    <polygon points="970,1448 1225,1448 1097,1488" fill="var(--slate)"/>
  </g>

  <!-- ===== Right panel: Quell Builders ===== -->
  <g class="panel panel--builders">
    <rect x="1401" y="100" width="609" height="1400" fill="var(--white)"/>
    <rect x="1401" y="265" width="609" height="320" fill="url(#grayFade)"/>
    <rect x="1401" y="265" width="609" height="320" fill="url(#haze)" role="img" aria-label="Construction cranes and hard hat linework over dark gray"/>
    <polygon points="1401,100 2010,100 2010,108 1818,108 1706,150 1594,108 1401,108" fill="var(--red)"/>
    <polygon points="1640,100 1772,100 1706,130" fill="var(--dark)"/>
    <polygon points="1401,180 2010,180 2010,265 1706,360 1401,265" fill="var(--white)"/>
    <polyline points="1401,260 1706,352 2010,260" fill="none" stroke="var(--red)" stroke-width="14"/>
    <polyline points="1450,258 1706,336 1964,258" fill="none" stroke="var(--white)" stroke-width="6"/>
    <rect x="1691" y="200" width="30" height="30" fill="var(--red)"/>
    <text class="brand-name" x="1706" y="296" text-anchor="middle">QUELL BUILDERS</text>

    <rect x="1401" y="810" width="609" height="690" fill="url(#lightFade)"/>
    <rect x="1401" y="810" width="609" height="260" fill="url(#haze)" role="img" aria-label="Crane and high-rise scaffolding linework over light gray"/>
    <rect x="1401" y="1400" width="609" height="100" fill="url(#blushFade)" role="img" aria-label="Red scaffolding linework on white"/>

    <polygon points="1401,585 1437,572 1972,572 2010,585 2010,790 1706,885 1401,790" fill="var(--white)"/>
    <polyline points="1401,580 1437,568" fill="none" stroke="var(--red)" stroke-width="8"/>
    <polyline points="1972,568 2010,580" fill="none" stroke="var(--red)" stroke-width="8"/>
    <rect x="1437" y="460" width="535" height="104" fill="var(--red)" stroke="var(--red)" stroke-width="5"/>
    <rect x="1441" y="464" width="527" height="96" fill="none" stroke="#e8585a" stroke-width="2"/>
    <text class="tagline" x="1706" y="529" text-anchor="middle">BUILD <tspan class="accent">SMARTER</tspan></text>

    <polygon points="1401,800 1706,895 2010,800 2010,815 1706,918 1401,815" fill="var(--red)"/>
    <polygon points="1401,790 1706,885 2010,790 2010,800 1706,897 1401,800" fill="var(--white)"/>

    <polygon points="1401,1070 1706,975 2010,1070 2010,1430 1706,1500 1401,1430" fill="var(--white)"/>
    <polygon points="1401,1080 1706,990 2010,1080 2010,1420 1706,1488 1401,1420" fill="url(#siteTone)"/>
    <polygon points="1401,1080 1706,990 2010,1080 2010,1420 1706,1488 1401,1420" fill="url(#siteGlow)" role="img" aria-label="Two construction engineers in hard hats and safety vests reviewing plans at a glass building"/>
    <polygon points="1578,1027 1706,990 1834,1027" fill="var(--red)"/>
    <polygon points="1578,1448 1834,1448 1706,1488" fill="var(--red)"/>

    <g class="services">
      <g class="icon"><rect x="1482" y="638" width="40" height="34" rx="3"/><path d="M1482 648 h40 M1490 660 l5 5 l9 -10 M1495 680 a12 12 0 0 1 24 0"/></g>
      <text class="service" x="1549" y="654">Construction</text>
      <text class="service" x="1549" y="684">Management</text>

      <g class="icon"><rect x="1740" y="640" width="42" height="44"/><path d="M1746 650 h14 M1746 658 h10 M1766 672 v-16 l8 6 v10 M1746 678 h30 M1748 636 h30"/></g>
      <text class="service" x="1808" y="654">Design+</text>
      <text class="service" x="1808" y="684">Build</text>

      <g class="icon"><circle cx="1500" cy="744" r="9"/><path d="M1488 744 a12 10 0 0 1 24 0 M1484 776 v-12 a16 12 0 0 1 32 0 v12 M1510 742 l12 -8 v34 h-6"/></g>
      <text class="service" x="1549" y="749">General</text>
      <text class="service" x="1549" y="779">Contracting</text>

      <g class="icon"><rect x="1738" y="738" width="46" height="36"/><circle cx="1780" cy="742" r="9"/><path d="M1780 737 v5 h4 M1744 768 l10 -12 l8 6 l12 -14 M1744 770 h34"/></g>
      <text class="service" x="1808" y="749">Pre-</text>
      <text class="service" x="1808" y="779">Construction</text>
    </g>
  </g>

  <line x1="791" y1="100" x2="791" y2="1500" stroke="rgba(0,0,0,0.08)" stroke-width="2"/>
  <line x1="1401" y1="100" x2="1401" y2="1500" stroke="rgba(0,0,0,0.08)" stroke-width="2"/>
</svg>
</body>
</html>
```